Restoration Specialist in need of business card designs

One side of the business card is a bathroom ripped out down to the studs with just a sink and toilet and then the other side is the bathroom (same sink and toilet) but put back together. Like a before and after on each side behind our information. Stand out, hard to forget, business cards for my restoration company. I want a unique concept all together.
Must include in no particular order:
our business name "Summit Renewals"
Possible Logo for a restoration company
Owner; Dennis Moravec
410-386-7294
dmoravec@summitrenewalsqx.example
SummitRenewalsQX.example (our company website) BUT I am open to any and all designs and options.

Target Market(s)

Customers, Men in the mitigation, plumbing, electrical, HVAC, Roofing, insurance companies

Industry/Entity Type

Restoration/ construction

Contact Information for Business Card

Must include in no particular order: our business name "Summit Renewals" Owner; Dennis Moravec 410-386-7294 dmoravec@summitrenewalsqx.example SummitRenewalsQX.example (our company website) MAY include a list of our services: Residential~ Emergency Response ~ Board- up~ Complete Restoration

Font styles to use
Serif

Colors
0054AA
0677BA
7BADD7
CADEEF
E8F1F8
F0912C
F2A743
F7CA91
FBE8D2
FDF5EE

Requirements
Must have
• unique, memorable, not something men have seen over and over again,
Nice to have
• eye catching
Should not have
• Been something I could have made by myself

```html
<!DOCTYPE html>
<html lang="en">
<head>
<meta charset="utf-8">
<title>Summit Renewals – Business Cards</title>
<link rel="stylesheet" href="https://fonts.googleapis.com/css2?family=Tinos:wght@400;700&display=swap">
<style>
  :root {
    --navy: #243a4f;
    --orange: #ee7a2a;
    --ink: #2a2a2a;
    --paper: #ffffff;
    --backdrop: #2b2b2d;
    --brand-tile: #f6f4f1;
  }
  * { box-sizing: border-box; margin: 0; padding: 0; }
  html, body {
    width: 1200px; height: 880px; overflow: hidden;
    background: var(--backdrop);
    font-family: "Tinos", "Times New Roman", serif;
  }
  .canvas {
    position: relative; width: 1200px; height: 880px;
  }
  .card {
    position: absolute; left: 240px; width: 720px; height: 400px;
    background: var(--paper); border-radius: 26px; overflow: hidden;
    box-shadow: 0 10px 30px rgba(0,0,0,.45);
  }
  .card--front { top: 30px; }
  .card--back { top: 450px; }

  /* brand lockup */
  .brand {
    position: absolute; display: flex; align-items: center; gap: 12px;
    background: var(--brand-tile); padding: 18px 22px;
  }
  .brand__mark { width: 22px; height: 22px; background: var(--orange); flex: none; }
  .brand__name {
    font-weight: 700; color: var(--navy); font-size: 34px; line-height: 1;
    white-space: nowrap;
  }
  .card--front .brand { left: 180px; top: 48px; }
  .card--back .brand { right: 60px; top: 36px; padding: 14px 18px; }
  .card--back .brand__name { font-size: 28px; }

  /* front services band */
  .services {
    position: absolute; left: 0; right: 0; bottom: 0; height: 178px;
    background: var(--navy); border-top: 4px solid var(--orange);
    box-shadow: 0 -5px 0 var(--paper);
    text-align: center; color: var(--paper);
    padding-top: 22px;
  }
  .card--front .services { top: auto; }
  .services__title {
    color: var(--orange); font-size: 22px; letter-spacing: .5px;
    margin-bottom: 8px;
  }
  .services__list { font-size: 23px; line-height: 1.3; }

  /* back details */
  .rule {
    position: absolute; height: 1.5px; background: var(--ink);
  }
  .rule--main { left: 36px; right: 60px; top: 214px; }
  .person { position: absolute; left: 52px; top: 148px; }
  .person__name { font-weight: 700; color: var(--navy); font-size: 34px; line-height: 1; }
  .person__role { color: var(--ink); font-size: 19px; margin-top: 4px; }
  .contacts {
    position: absolute; left: 52px; top: 238px; list-style: none;
    font-size: 19px; color: var(--ink);
  }
  .contacts li { display: flex; align-items: center; gap: 12px; height: 32px; }
  .contacts svg { width: 20px; height: 20px; fill: var(--navy); flex: none; }
  .address {
    position: absolute; right: 56px; top: 240px; text-align: right;
    font-size: 18px; color: var(--ink); line-height: 1.3;
  }
</style>
</head>
<body>
<main class="canvas">

  <section class="card card--front" aria-label="Business card front">
    <div class="brand">
      <span class="brand__mark"></span>
      <span class="brand__name">Summit Renewals</span>
    </div>
    <div class="services">
      <p class="services__title">OUR SERVICES:</p>
      <p class="services__list">Residential • Emergency Response • Board- up<br>• Storm Protection • Complete Restoration</p>
    </div>
  </section>

  <section class="card card--back" aria-label="Business card back">
    <div class="brand">
      <span class="brand__mark"></span>
      <span class="brand__name">Summit Renewals</span>
    </div>
    <div class="person">
      <h1 class="person__name">Dennis Moravec</h1>
      <p class="person__role">Owner</p>
    </div>
    <div class="rule rule--main"></div>
    <ul class="contacts">
      <li>
        <svg viewBox="0 0 24 24" aria-hidden="true"><path d="M6.6 10.8a15.1 15.1 0 0 0 6.6 6.6l2.2-2.2a1 1 0 0 1 1-.25 11.4 11.4 0 0 0 3.6.57 1 1 0 0 1 1 1V20a1 1 0 0 1-1 1A17 17 0 0 1 3 4a1 1 0 0 1 1-1h3.5a1 1 0 0 1 1 1c0 1.25.2 2.45.57 3.57a1 1 0 0 1-.25 1z"/></svg>
        <span>410-386-7294</span>
      </li>
      <li>
        <svg viewBox="0 0 24 24" aria-hidden="true"><path d="M2 5h20v14H2z M2 5l10 8 10-8" /></svg>
        <span>dmoravec@summitrenewalsqx.example</span>
      </li>
      <li>
        <svg viewBox="0 0 24 24" aria-hidden="true"><path fill-rule="evenodd" d="M12 2a10 10 0 1 1 0 20 10 10 0 0 1 0-20zm0 2a8 8 0 0 0-6.9 12l2.4-1.6-.5-2.4 2-1.5V7.5l2.5-1.5L14 7l-1 2 2.5 1.5 2.5-.5 1 3a8 8 0 0 0-7-9z"/></svg>
        <span>SummitRenewalsQX.example</span>
      </li>
    </ul>
    <address class="address">421, Address line goes here<br>45452, Country name</address>
  </section>

</main>
</body>
</html>
```